Fresh, modern, fun business card for pediatric dental practice

Need a business card for fresh, modern, fun pediatric dental practice

Clean look that matches our website's font and colors

We prefer the look of curved corners on business cards

Target Market(s)

parents (mothers) of young children, professionals, mid-high class

Industry/Entity Type

Dental

Contact Information for Business Card

Maplebrook Pediatric Dentistry
482 Orchard Vale Road
Suite 517
Fernhollow, PA 17999
555.419.3067
www.maplebrookkidsdental.example

Mara Tevlin, DMD
Colette Varnum, DMD
(we are working on our email address, but we would like that on the card as well)

Font styles to use
Sans Serif

Requirements
Must have
• All info; we would also like to make cards for individual staff members
• colors from our website and color palatte, attatched
• use same font and design as website for branding
Nice to have
• clean, simple card that has a pop of color
• we would like to see a few designs with our tag line "where little grins grow"
• we are not sure if we want to have it on there or not
• we would like to see a few designs incorporating the ribbon graphic on our website where the word WELCOME is

```html
<!DOCTYPE html>
<html lang="en">
<head>
<meta charset="utf-8">
<title>Maplebrook Pediatric Dentistry – Business Card</title>
<link rel="stylesheet" href="https://fonts.googleapis.com/css2?family=Roboto:wght@400;500&family=Roboto+Slab:wght@400&display=swap">
<style>
  :root {
    --plum: #55264f;
    --plum-light: #733d76;
    --pink: #d3408f;
    --gold: #f6b52a;
    --white: #ffffff;
    --backdrop: #ece7df;
    --text: #4a2148;
  }
  * { box-sizing: border-box; margin: 0; padding: 0; }
  html, body { width: 900px; height: 1200px; overflow: hidden; }
  body {
    position: relative;
    background: var(--backdrop);
    font-family: "Roboto", Arial, sans-serif;
    color: var(--text);
  }
  .card {
    position: absolute;
    left: 82px;
    width: 733px;
    height: 430px;
    border-radius: 22px;
    overflow: hidden;
    box-shadow: 0 6px 14px rgba(60, 40, 20, 0.25);
  }
  .card-front { top: 137px; background: var(--white); }
  .card-back {
    top: 633px;
    background: linear-gradient(90deg, var(--plum) 0%, var(--plum-light) 100%);
  }
  .dentists {
    position: absolute; left: 41px; top: 52px;
    font-size: 22px; font-weight: 500; line-height: 31px;
  }
  .dentists .credential { color: var(--pink); font-weight: 400; }
  .address {
    position: absolute; left: 41px; top: 177px;
    font-size: 16.5px; line-height: 29px; font-style: normal;
  }
  .contacts {
    position: absolute; left: 41px; top: 249px;
    list-style: none; font-size: 16.5px;
  }
  .contacts li { display: flex; align-items: center; height: 31.5px; }
  .contacts svg { width: 26px; height: 26px; margin-right: 11px; flex: none; }
  .brand {
    position: absolute; text-align: center; color: var(--gold);
    font-weight: 500; line-height: 1.1;
  }
  .brand .mark {
    display: block; margin: 0 auto 14px;
    width: 46px; height: 46px; border-radius: 50%; background: var(--gold);
  }
  .brand .name-main { display: block; font-size: 46px; }
  .brand .name-sub { display: block; font-size: 25px; letter-spacing: 0.5px; }
  .card-front .brand { left: 370px; width: 340px; top: 110px; }
  .card-back .brand { left: 0; width: 733px; top: 110px; }
  .card-back .brand .mark { width: 58px; height: 58px; margin-bottom: 18px; }
  .card-back .brand .name-main { font-size: 64px; }
  .card-back .brand .name-sub { font-size: 33px; }
  .tagline-band {
    position: absolute; left: 0; top: 378px; width: 100%; height: 34px;
    background: var(--plum); color: var(--white);
    font-family: "Roboto Slab", "Roboto", sans-serif;
    font-size: 18.5px; text-align: center; line-height: 34px;
  }
</style>
</head>
<body>
  <section class="card card-front">
    <div class="dentists">
      <div>Mara Tevlin, <span class="credential">DMD</span></div>
      <div>Colette Varnum, <span class="credential">DMD</span></div>
    </div>
    <address class="address">
      482 Orchard Vale Road<br>
      Suite 517, Fernhollow, PA 17999
    </address>
    <ul class="contacts">
      <li>
        <svg viewBox="0 0 26 26" aria-hidden="true"><circle cx="13" cy="13" r="13" fill="var(--pink)"/><path d="M7 11c0-2 2-3 6-3s6 1 6 3l-2 1-1-2h-6l-1 2zM9 13h8l1 5H8z" fill="#fff"/></svg>
        555.419.3067
      </li>
      <li>
        <svg viewBox="0 0 26 26" aria-hidden="true"><circle cx="13" cy="13" r="13" fill="var(--pink)"/><rect x="7" y="8.5" width="12" height="9" rx="1" fill="#fff"/><path d="M7.5 9.5l5.5 4.5 5.5-4.5" fill="none" stroke="var(--pink)" stroke-width="1.3"/></svg>
        info@maplebrookkidsdental.example
      </li>
      <li>
        <svg viewBox="0 0 26 26" aria-hidden="true"><circle cx="13" cy="13" r="13" fill="var(--pink)"/><g fill="none" stroke="#fff" stroke-width="1.3"><circle cx="13" cy="13" r="6.5"/><ellipse cx="13" cy="13" rx="3" ry="6.5"/><path d="M6.5 13h13M7.5 10h11M7.5 16h11"/></g></svg>
        www.maplebrookkidsdental.example
      </li>
    </ul>
    <div class="brand">
      <span class="mark"></span>
      <span class="name-main">Maplebrook</span>
      <span class="name-sub">Pediatric Dentistry</span>
    </div>
    <div class="tagline-band">where little grins grow</div>
  </section>

  <section class="card card-back">
    <div class="brand">
      <span class="mark"></span>
      <span class="name-main">Maplebrook</span>
      <span class="name-sub">Pediatric Dentistry</span>
    </div>
  </section>
</body>
</html>
```